Banner Ad Design Project

I have a digital X Ray blog. I need a header to fit my WP theme.
Please visit the site and let me know what you think. I am open to other design ideas not only the banner. I want the to be clean and professional.

Thank you
www.BrightPlateScan.com

Target Market(s)

Medical Doctors, Orthopedic Surgeon, X-Ray equipment Dealers,

Industry/Entity Type

Digital

```html
<!DOCTYPE html>
<html lang="en">
<head>
<meta charset="utf-8">
<title>Wireless Digital X-ray Flat Panel Detector</title>
<link rel="stylesheet" href="https://fonts.googleapis.com/css2?family=Source+Sans+3:ital,wght@0,400;1,700&display=swap">
<style>
  :root {
    --bg-light: #f3f4f6;
    --bg-mid: #e4e6e9;
    --bg-edge: #d9dce0;
    --title-blue: #1c5fa8;
    --tagline-grey: #3b3f44;
    --rule: #c3c7cc;
    --band: rgba(255, 255, 255, 0.9);
  }
  * { margin: 0; padding: 0; box-sizing: border-box; }
  html, body { width: 1200px; height: 194px; overflow: hidden; }
  body { background: var(--bg-light); }

  .header-banner {
    position: relative;
    width: 1200px;
    height: 194px;
    overflow: hidden;
    background: linear-gradient(180deg, var(--bg-light) 0%, var(--bg-mid) 70%, var(--bg-edge) 100%);
  }

  .device-visual {
    position: absolute;
    right: 0;
    top: 0;
    width: 560px;
    height: 194px;
    background: linear-gradient(90deg, rgba(255,255,255,0) 0%, rgba(250,250,251,0.8) 40%, rgba(238,240,242,0.9) 100%);
  }

  .title-band {
    position: absolute;
    left: 0;
    top: 60px;
    width: 1100px;
    height: 62px;
    background: linear-gradient(90deg, var(--band) 0%, var(--band) 60%, rgba(255,255,255,0) 100%);
  }

  .banner-title {
    position: absolute;
    left: 48px;
    top: 54px;
    font-family: "Source Sans 3", sans-serif;
    font-style: italic;
    font-weight: 700;
    font-size: 56px;
    line-height: 64px;
    color: var(--title-blue);
    letter-spacing: -0.3px;
    white-space: nowrap;
  }

  .banner-tagline {
    position: absolute;
    left: 58px;
    top: 126px;
    font-family: "Source Sans 3", sans-serif;
    font-weight: 400;
    font-size: 24px;
    line-height: 28px;
    letter-spacing: 2.2px;
    text-transform: uppercase;
    color: var(--tagline-grey);
    white-space: nowrap;
  }

  .tagline-rule {
    position: absolute;
    left: 0;
    top: 162px;
    width: 800px;
    height: 1px;
    background: linear-gradient(90deg, var(--rule) 0%, var(--rule) 50%, rgba(195,199,204,0) 100%);
  }
</style>
</head>
<body>
  <header class="header-banner">
    <div class="device-visual" role="img" aria-label="Faint photo of a wireless flat panel X-ray detector"></div>
    <div class="title-band"></div>
    <h1 class="banner-title">Wireless Digital X-ray Flat Panel Detector</h1>
    <p class="banner-tagline">The simple way to upgrade to DR</p>
    <div class="tagline-rule"></div>
  </header>
</body>
</html>
```